need a clean, modern job advertisement designed for social media (Facebook & Instagram).

The post is to advertise two positions:
• Leading Hand Boilermaker
• Dragline Fitter
We want the design to match our KRT Plant Services branding: blue, white, strong, professional, mining-industry style.
What the design should include:
Bold headline: “WE’RE HIRING”
Sub-headline: “Leading Hand Boilermaker & Dragline Fitter”
Key points:
• Bowen Basin based
• Dragline & shovel maintenance
• Great pay + long-term work
• Locally owned & operated
KRT logo placed cleanly
Space for 1–2 images (boilermaking or dragline work)
Design style:
Strong and industrial
Blue/white colour scheme
Easy to read at a glance
Suitable for a square 1080×1080 design

```html
<!DOCTYPE html>
<html lang="en">
<head>
<meta charset="utf-8">
<title>KRT Plant Services – We're Hiring</title>
<link rel="stylesheet" href="https://fonts.googleapis.com/css2?family=Bebas+Neue&family=Oswald:wght@500;600&display=swap">
<style>
  :root {
    --stage: #2b2b2d;
    --black: #050608;
    --blue: #0aa8f0;
    --blue-deep: #0a6fb3;
    --white: #ffffff;
    --gold: #f7c600;
    --photo-warm-a: #2a1a10;
    --photo-warm-b: #b8692a;
    --photo-sky-a: #0d3f9a;
    --photo-sky-b: #5a8fbf;
  }
  * { margin: 0; padding: 0; box-sizing: border-box; }
  html, body { width: 1200px; height: 675px; overflow: hidden; }
  body {
    background: radial-gradient(ellipse at 50% 45%, #3a3a3c 0%, var(--stage) 70%);
    position: relative;
    font-family: "Oswald", "Bebas Neue", sans-serif;
  }
  .post {
    position: absolute;
    top: 100px;
    width: 486px;
    height: 486px;
    overflow: hidden;
    background:
      radial-gradient(ellipse 75% 60% at 0% 0%, rgba(10,120,200,.85) 0%, rgba(10,60,110,.35) 45%, transparent 75%),
      var(--black);
    box-shadow: 0 24px 30px -18px rgba(0,0,0,.7);
  }
  .post--blue { left: 91px; }
  .post--gold { left: 616px; }

  .post__photo { position: absolute; inset: 0; }
  .post__photo svg { width: 486px; height: 486px; display: block; }

  .brand {
    position: absolute;
    left: 330px; top: 58px;
    width: 140px;
    display: flex; align-items: center; gap: 6px;
    font-family: "Bebas Neue", sans-serif;
    font-size: 22px; line-height: 1;
    color: var(--white);
    letter-spacing: .5px;
  }
  .brand__dot {
    flex: none;
    width: 16px; height: 16px; border-radius: 50%;
    background: var(--blue);
  }

  .headline {
    position: absolute;
    left: 27px; top: 22px;
    font-family: "Bebas Neue", sans-serif;
    font-size: 116px;
    line-height: 88px;
    color: var(--blue);
    letter-spacing: -1px;
  }
  .post--gold .headline span {
    background: linear-gradient(90deg, var(--gold) 0%, #f4e7b0 30%, #e8f3fb 50%, #7ccaf0 75%, var(--blue) 100%);
    -webkit-background-clip: text; background-clip: text;
    color: transparent;
  }
  .headline span { display: block; }

  .role {
    position: absolute;
    left: 26px;
    height: 32px;
    display: flex; align-items: center; gap: 8px;
    padding-left: 8px;
    border-radius: 16px;
    background: var(--white);
    color: var(--black);
    font-family: "Bebas Neue", sans-serif;
    font-size: 22px; letter-spacing: .3px;
  }
  .role svg { width: 22px; height: 22px; flex: none; }
  .role--one { top: 237px; width: 274px; }
  .role--two { top: 280px; width: 274px; }
  .post--gold .role {
    background: transparent;
    border: 1px solid var(--white);
    color: var(--white);
    font-family: "Oswald", sans-serif;
    font-weight: 600; font-size: 17px; letter-spacing: -.6px;
  }
  .post--gold .role--one { width: 242px; }
  .post--gold .role--two { width: 162px; }

  .perks { position: absolute; left: 34px; top: 350px; width: 260px; height: 70px; }
  .perk {
    position: absolute;
    display: flex; align-items: center; gap: 6px;
    color: var(--white);
    font-family: "Oswald", sans-serif; font-weight: 500;
    font-size: 10.5px; line-height: 11px; letter-spacing: .2px;
    text-transform: uppercase;
  }
  .perk__num {
    width: 22px; height: 23px;
    background: var(--blue);
    color: var(--white);
    font-family: "Bebas Neue", sans-serif;
    font-size: 22px; line-height: 24px; text-align: center;
  }
  .post--gold .perk__num { background: var(--gold); }
  .perk--1 { left: 0; top: 0; }
  .perk--3 { left: 116px; top: 0; }
  .perk--2 { left: 0; top: 43px; }
  .perk--4 { left: 116px; top: 44px; }

  .web {
    position: absolute;
    left: 0; top: 446px;
    width: 270px; height: 22px;
    display: flex; align-items: center; gap: 7px;
    padding-left: 34px;
    background: linear-gradient(90deg, var(--blue) 0%, var(--blue-deep) 22%, rgba(10,60,110,.6) 70%, transparent 100%);
    color: var(--white);
    font-family: "Bebas Neue", sans-serif;
    font-size: 17px; letter-spacing: .4px;
  }
  .web svg { width: 15px; height: 15px; flex: none; }
</style>
</head>
<body>

  <article class="post post--blue">
    <div class="post__photo">
      <svg viewBox="0 0 486 486" aria-hidden="false">
        <defs>
          <linearGradient id="warmA" x1="0" y1="0" x2="0.4" y2="1">
            <stop offset="0" stop-color="var(--photo-warm-a)"/>
            <stop offset=".5" stop-color="#6a3d1c"/>
            <stop offset="1" stop-color="var(--photo-warm-b)"/>
          </linearGradient>
          <linearGradient id="skyA" x1="0" y1="0" x2="0" y2="1">
            <stop offset="0" stop-color="var(--photo-sky-a)"/>
            <stop offset="1" stop-color="var(--photo-sky-b)"/>
          </linearGradient>
        </defs>
        <polygon role="img" aria-label="Photo of a welder at work with sparks" points="356,0 486,0 486,486 416,486 252,144" fill="url(#warmA)"/>
        <polygon role="img" aria-label="Photo of a dragline at a mine site" points="322,331 416,486 234,486" fill="url(#skyA)"/>
      </svg>
    </div>
    <div class="brand"><span class="brand__dot"></span>KRT Plant Services</div>
    <h1 class="headline"><span>We’re</span><span>Hiring</span></h1>
    <div class="role role--one">
      <svg viewBox="0 0 24 24"><circle cx="10" cy="10" r="7.5" fill="none" stroke="var(--blue)" stroke-width="3"/><line x1="15.5" y1="15.5" x2="22" y2="22" stroke="var(--blue)" stroke-width="3.2" stroke-linecap="round"/></svg>
      Leading Hand Boilermaker
    </div>
    <div class="role role--two">
      <svg viewBox="0 0 24 24"><circle cx="10" cy="10" r="7.5" fill="none" stroke="var(--blue)" stroke-width="3"/><line x1="15.5" y1="15.5" x2="22" y2="22" stroke="var(--blue)" stroke-width="3.2" stroke-linecap="round"/></svg>
      Dragline Fitter
    </div>
    <div class="perks">
      <div class="perk perk--1"><span class="perk__num">01</span><span>Bowen Basin<br>Based</span></div>
      <div class="perk perk--3"><span class="perk__num">03</span><span>Dragline &amp; Shovel<br>Maintenance</span></div>
      <div class="perk perk--2"><span class="perk__num">02</span><span>Great Pay +<br>Long-Term Work</span></div>
      <div class="perk perk--4"><span class="perk__num">04</span><span>Locally Owned<br>&amp; Operated</span></div>
    </div>
    <div class="web">
      <svg viewBox="0 0 24 24" fill="none" stroke="var(--white)" stroke-width="1.8"><circle cx="12" cy="12" r="10"/><ellipse cx="12" cy="12" rx="4.5" ry="10"/><line x1="2" y1="12" x2="22" y2="12"/><path d="M4 6.5h16M4 17.5h16"/></svg>
      www.krtplantservices.com
    </div>
  </article>

  <article class="post post--gold">
    <div class="post__photo">
      <svg viewBox="0 0 486 486">
        <defs>
          <linearGradient id="warmB" x1="0" y1="0" x2="0.4" y2="1">
            <stop offset="0" stop-color="var(--photo-warm-a)"/>
            <stop offset=".5" stop-color="#6a3d1c"/>
            <stop offset="1" stop-color="var(--photo-warm-b)"/>
          </linearGradient>
          <linearGradient id="skyB" x1="0" y1="0" x2="0" y2="1">
            <stop offset="0" stop-color="var(--photo-sky-a)"/>
            <stop offset="1" stop-color="var(--photo-sky-b)"/>
          </linearGradient>
        </defs>
        <polygon role="img" aria-label="Photo of a welder at work with sparks" points="356,0 486,0 486,486 416,486 252,144" fill="url(#warmB)"/>
        <polygon role="img" aria-label="Photo of a dragline at a mine site" points="322,331 416,486 234,486" fill="url(#skyB)"/>
      </svg>
    </div>
    <div class="brand"><span class="brand__dot"></span>KRT Plant Services</div>
    <h1 class="headline"><span>We’re</span><span>Hiring</span></h1>
    <div class="role role--one">
      <svg viewBox="0 0 24 24"><circle cx="10" cy="10" r="7.5" fill="none" stroke="var(--blue)" stroke-width="3"/><line x1="15.5" y1="15.5" x2="22" y2="22" stroke="var(--blue)" stroke-width="3.2" stroke-linecap="round"/></svg>
      Leading Hand Boilermaker
    </div>
    <div class="role role--two">
      <svg viewBox="0 0 24 24"><circle cx="10" cy="10" r="7.5" fill="none" stroke="var(--blue)" stroke-width="3"/><line x1="15.5" y1="15.5" x2="22" y2="22" stroke="var(--blue)" stroke-width="3.2" stroke-linecap="round"/></svg>
      Dragline Fitter
    </div>
    <div class="perks">
      <div class="perk perk--1"><span class="perk__num">01</span><span>Bowen Basin<br>Based</span></div>
      <div class="perk perk--3"><span class="perk__num">03</span><span>Dragline &amp; Shovel<br>Maintenance</span></div>
      <div class="perk perk--2"><span class="perk__num">02</span><span>Great Pay +<br>Long-Term Work</span></div>
      <div class="perk perk--4"><span class="perk__num">04</span><span>Locally Owned<br>&amp; Operated</span></div>
    </div>
    <div class="web">
      <svg viewBox="0 0 24 24" fill="none" stroke="var(--white)" stroke-width="1.8"><circle cx="12" cy="12" r="10"/><ellipse cx="12" cy="12" rx="4.5" ry="10"/><line x1="2" y1="12" x2="22" y2="12"/><path d="M4 6.5h16M4 17.5h16"/></svg>
      www.krtplantservices.com
    </div>
  </article>

</body>
</html>
```